Northwind Trade Allies - Letterhead and Folder

I am looking for letterhead that uses the splash from the logo on the side of the page as well as some information from our website.

I am looking for a folder that is a fold out that has pockets to hold paper as well as a slits for a business card.

Website address is www.northwindtradeallies.example

Target Market(s)

Export of Agrifoods, commodities and emergency aid.
Supplying the world food security.

Requirements
Must have
• Use splash and logo, have information about company.
• Letterhead must have splash on a side not in the middle.
Nice to have
• Different pictures that what are provided.

```html
<!DOCTYPE html>
<html lang="en">
<head>
<meta charset="utf-8">
<title>Northwind Trade Allies – Letterhead and Folder</title>
<link href="https://fonts.googleapis.com/css2?family=Roboto:wght@400;500&display=swap" rel="stylesheet">
<style>
  :root {
    --backdrop: #b9b9bb;
    --paper: #ffffff;
    --ink: #1d1d1f;
    --ink-soft: #2c2c2e;
    --teal: #0e8591;
    --green: #3a9a46;
    --field-top: #9fa933;
    --field-bottom: #3f5a20;
    --photo-a: #8f9c35;
    --photo-b: #c3c23a;
    --photo-c: #a9b238;
    --sig: #ececec;
    --splash: #e9eef0;
  }
  * { margin: 0; padding: 0; box-sizing: border-box; }
  html, body { width: 1189px; height: 1200px; overflow: hidden; background: var(--backdrop); }
  body { position: relative; font-family: "Roboto", Arial, sans-serif; color: var(--ink); }

  .sheet { position: absolute; background: var(--paper); overflow: hidden; }
  .letterhead { left: 34px; top: 260px; width: 526px; height: 680px; }
  .folder { left: 635px; top: 260px; width: 524px; height: 677px; }

  .side-splash { position: absolute; left: -150px; top: 150px; width: 430px; height: 430px; border-radius: 50%;
    background: radial-gradient(circle, var(--splash) 0%, rgba(233,238,240,0.5) 55%, rgba(255,255,255,0) 72%); }

  .brand { position: absolute; display: flex; align-items: center; }
  .brand-mark { border-radius: 50%; border: 2px solid var(--green); flex: none; }
  .brand-name { font-weight: 500; text-transform: uppercase; color: var(--ink); letter-spacing: 0.04em; line-height: 1; white-space: nowrap; }

  .letterhead .brand { left: 41px; top: 45px; gap: 10px; }
  .letterhead .brand-mark { width: 56px; height: 56px; }
  .letterhead .brand-name { font-size: 14px; }

  .contact { position: absolute; left: 337px; top: 58px; border-left: 1px solid var(--teal); padding-left: 8px; font-size: 8px; line-height: 9.5px; color: var(--ink-soft); list-style: none; }
  .contact li { display: flex; align-items: center; gap: 4px; }
  .contact svg { width: 7px; height: 7px; flex: none; }

  .recipient { position: absolute; left: 41px; top: 192px; font-size: 8.5px; line-height: 10.5px; }
  .recipient-name { font-size: 10.5px; font-weight: 500; margin-bottom: 4px; }

  .body-copy { position: absolute; left: 41px; top: 274px; width: 442px; font-size: 9.4px; line-height: 15.5px; text-align: justify; color: var(--ink-soft); }
  .body-copy p + p { margin-top: 15px; }

  .signoff { position: absolute; left: 41px; top: 513px; font-size: 9.4px; }
  .signature { position: absolute; left: 41px; top: 534px; width: 122px; height: 34px; background: var(--sig); border-radius: 3px; }
  .signer { position: absolute; left: 41px; top: 578px; font-size: 9.4px; line-height: 12px; }
  .signer-name { font-weight: 500; font-size: 10px; }

  .band { position: absolute; left: 0; bottom: 0; width: 100%; height: 29px; background: var(--teal); }

  .folder .brand { left: 92px; top: 55px; gap: 16px; }
  .folder .brand-mark { width: 86px; height: 86px; border-width: 3px; }
  .folder .brand-name { font-size: 19px; }

  .field { position: absolute; left: 0; top: 0; width: 524px; height: 677px; }
  .folder-url { position: absolute; left: 0; width: 100%; top: 652px; text-align: center; font-size: 8.5px; color: var(--ink-soft); }
</style>
</head>
<body>

<section class="sheet letterhead">
  <div class="side-splash" role="img" aria-label="Faint brand splash along the left side"></div>

  <div class="brand">
    <span class="brand-mark"></span>
    <span class="brand-name">Northwind Trade Allies</span>
  </div>

  <ul class="contact">
    <li><svg viewBox="0 0 8 8"><rect width="8" height="8" fill="#0e8591"/><path d="M2 1.5l1 1-0.6.8a4 4 0 0 0 2.3 2.3l.8-.6 1 1-.8.9C3.6 6.8 1.2 4.4 1.1 2.3z" fill="#fff"/></svg>555 014 2280</li>
    <li><svg viewBox="0 0 8 8"><rect width="8" height="8" fill="#0e8591"/><rect x="1.5" y="2.2" width="5" height="3.6" fill="#fff"/></svg>hello@northwindtradeallies.example</li>
    <li><svg viewBox="0 0 8 8"><rect width="8" height="8" fill="#0e8591"/><circle cx="4" cy="4" r="2.4" fill="none" stroke="#fff" stroke-width=".8"/></svg>www.northwindtradeallies.example</li>
  </ul>

  <div class="recipient">
    <p class="recipient-name">EVAN MARLOW</p>
    <p>Street Name,City Name.</p>
    <p>Zip Coad 0000</p>
  </div>

  <div class="body-copy">
    <p>Lorem Ipsum is simply dummy text of the printing and typesetting industry. Lorem Ipsum has been the industry's standard dummy text ever since the 1500s, when an unknown printer took a galley of type and scrambled it to make a type specimen book. It has survived not only five centuries,but also the leap into electronic typesetting, remaining essentially unchanged. It was popularised in the 1960s with the release of Letraset sheets containing Lorem Ipsum passages, and more recently with desktop publishing software like Aldus PageMaker including versions of Lorem Ipsum.</p>
    <p>It is a long established fact that a reader will be distracted by the readable content of a page when looking at its layout. The point of using Lorem Ipsum is that it has a more-or-less normal distribution of letters, as opposed to using 'Content here, content here', making it look like readable English. Many desktop and publishing packages and web page editors now use Lorem Ipsum as their default model text, and a search for 'lorem ipsum' will uncover many web sites still in their infancy. Various versions have evolved over the years, sometimes by accident, sometimes on purpose (injected humour and the like).</p>
  </div>

  <p class="signoff">Regards,</p>
  <div class="signature" role="img" aria-label="Handwritten signature"></div>
  <div class="signer">
    <p class="signer-name">Clara Wendt</p>
    <p>General Maneger</p>
  </div>

  <div class="band"></div>
</section>

<section class="sheet folder">
  <div class="brand">
    <span class="brand-mark"></span>
    <span class="brand-name">Northwind Trade Allies</span>
  </div>

  <svg class="field" viewBox="0 0 524 677">
    <defs>
      <linearGradient id="crop" x1="0" y1="0" x2="0" y2="1">
        <stop offset="0" stop-color="#9fa933"/>
        <stop offset="1" stop-color="#3f5a20"/>
      </linearGradient>
    </defs>
    <path d="M0 271 Q270 255 524 395 V640 H0 Z" fill="url(#crop)" role="img" aria-label="Photo of a flowering yellow crop field"/>
    <circle cx="97" cy="262" r="55" fill="#fff" stroke="#3a9a46" stroke-width="2"/>
    <circle cx="97" cy="262" r="49" fill="#8f9c35" role="img" aria-label="Photo of a farm road between crop fields"/>
    <circle cx="269" cy="288" r="55" fill="#fff" stroke="#3a9a46" stroke-width="2"/>
    <circle cx="269" cy="288" r="49" fill="#c3c23a" role="img" aria-label="Photo of a wide yellow field"/>
    <circle cx="434" cy="337" r="55" fill="#fff" stroke="#3a9a46" stroke-width="2"/>
    <circle cx="434" cy="337" r="49" fill="#a9b238" role="img" aria-label="Close-up photo of yellow blossoms"/>
  </svg>

  <p class="folder-url">www.northwindtradeallies.example</p>
</section>

</body>
</html>
```